Business Card Design

A business card design must match as a cleaning company.
We do house cleaning, office, cafe , function center , club and so on.

Industry/Entity Type

House

Contact Information for Business Card

Silver Fern cleaning services
Marla Voss
Director
0429385716
1300 862 419
Silverfern.cleaning@examplemail.com

```html
<!DOCTYPE html>
<html lang="en">
<head>
<meta charset="utf-8">
<title>Silver Fern Cleaning Services – Business Card</title>
<link rel="stylesheet" href="https://fonts.googleapis.com/css2?family=Play:wght@400;700&display=swap">
<style>
  :root {
    --mint: #d8efeb;
    --floor: #bfbfc3;
    --teal: #5f9c91;
    --ink: #0d0d0d;
    --brand-ink: #2b3338;
    --hair: #8a4f22;
    --dress: #f4d33a;
  }
  * { margin: 0; padding: 0; box-sizing: border-box; }
  html, body { width: 1200px; height: 740px; overflow: hidden; background: #ffffff; }
  .card {
    position: relative;
    width: 1200px;
    height: 740px;
    overflow: hidden;
    background: var(--mint);
    font-family: "Play", sans-serif;
  }
  .card__backdrop { position: absolute; inset: 0; }
  .card__illustration {
    position: absolute;
    left: 42px;
    top: 112px;
    width: 370px;
    height: 580px;
    border-radius: 140px 140px 60px 60px;
    background: linear-gradient(180deg, var(--hair) 0%, #b77a3c 35%, var(--dress) 60%, #f29a2e 80%, #d9dadf 100%);
    opacity: 0.85;
  }
  .brand {
    position: absolute;
    left: 430px;
    top: 82px;
    width: 700px;
    text-align center;
    text-align: center;
    color: var(--brand-ink);
    font-family: "Play", sans-serif;
    font-weight: 700;
    font-size: 64px;
    line-height: 72px;
  }
  .services {
    position: absolute;
    left: 430px;
    top: 246px;
    width: 700px;
    text-align: center;
    color: var(--teal);
    font-size: 27px;
    line-height: 36px;
    letter-spacing: 4px;
  }
  .contact {
    position: absolute;
    left: 480px;
    top: 372px;
    width: 600px;
    text-align: center;
  }
  .contact__role {
    color: var(--teal);
    font-size: 30px;
    line-height: 36px;
  }
  .contact__name {
    color: var(--ink);
    font-size: 58px;
    line-height: 60px;
  }
  .contact__phones {
    margin-top: 2px;
    color: var(--ink);
    font-size: 35px;
    line-height: 40px;
    font-weight: 700;
    letter-spacing: 0.5px;
  }
  .contact__email {
    position: absolute;
    left: 440px;
    top: 622px;
    width: 660px;
    text-align: center;
    color: var(--ink);
    font-size: 30px;
    font-weight: 700;
    letter-spacing: 0.3px;
  }
</style>
</head>
<body>
  <main class="card">
    <svg class="card__backdrop" width="1200" height="740" viewBox="0 0 1200 740" aria-hidden="true">
      <polygon points="0,466 1200,579 1200,740 0,740" fill="var(--floor)"/>
      <g fill="#ffffff" opacity="0.35">
        <polygon points="60,740 150,740 760,0 670,0"/>
        <polygon points="230,740 270,740 880,0 840,0"/>
        <polygon points="430,740 540,740 1150,0 1040,0"/>
        <polygon points="640,740 680,740 1200,110 1200,60"/>
        <polygon points="820,740 920,740 1200,400 1200,280"/>
      </g>
      <ellipse cx="210" cy="560" rx="230" ry="55" fill="#9a9ba0" opacity="0.45"/>
    </svg>

    <div class="card__illustration" role="img" aria-label="Illustration of a child with braided hair wiping a window with a cloth"></div>

    <h1 class="brand">Silver Fern<br>Cleaning Services</h1>

    <p class="services">House Cleaning, Office, Cafe,<br>Function Center, Club’s.</p>

    <section class="contact">
      <p class="contact__role">Director</p>
      <p class="contact__name">Marla Voss</p>
      <p class="contact__phones">0429385716 1300 862 419</p>
    </section>

    <p class="contact__email">Silverfern.cleaning@examplemail.com</p>
  </main>
</body>
</html>
```